need professional, precise design for a website

I will start with a homepage design and if we pick your design, we'll have you design up to 6 more interior pages (we'll pay extra for these of course). We need a homepage design for a reserve study company based in Idaho, covering the northwest region. The company is called copper ridge reserve study. Their current site is at https://www.copperridgereserves.example/ and they really like this site for inspiration https://www.fundplannerhub.example/ but they would like an original design, just more modern and fresh like the sample site. I have logo files I will attach. They want something that looks financial and has a feel of accuity. Their main call to action will be to have someone fill in a contact form or call them on the phone. They will have a sample study that someone can download as on the fundplannerhub site. You can use copy from their current site.

```html
<!DOCTYPE html>
<html lang="en">
<head>
<meta charset="utf-8">
<title>Copper Ridge Reserves – Association Analytics</title>
<link href="https://fonts.googleapis.com/css2?family=Playfair+Display:wght@700&family=Roboto:ital,wght@0,300;0,400;0,500;1,400&display=swap" rel="stylesheet">
<style>
  :root{
    --navy:#221d5a;
    --navy-text:#2a2566;
    --green:#4e9a2a;
    --white:#ffffff;
    --body:#5b5b66;
    --hero-dark:#2b2c30;
  }
  *{margin:0;padding:0;box-sizing:border-box}
  html,body{width:1200px;height:1200px;overflow:hidden;background:var(--white);font-family:"Roboto",sans-serif}
  .page{position:relative;width:1200px;height:1200px;overflow:hidden}

  /* hero */
  .hero{position:absolute;left:0;top:0;width:1200px;height:647px;border-bottom-right-radius:110px;overflow:hidden;
    background:radial-gradient(ellipse at 55% 45%,#4a4a4c 0%,#37383b 45%,var(--hero-dark) 100%)}
  .header-line{position:absolute;left:22px;right:20px;top:73px;height:1px;background:rgba(255,255,255,.18)}
  .brand{position:absolute;left:28px;top:22px;display:flex;align-items:center;gap:10px;color:var(--white)}
  .brand-dot{width:30px;height:30px;border:2px solid var(--white);border-radius:50%}
  .brand-name{font-size:21px;font-weight:400;letter-spacing:.5px}
  .nav{position:absolute;top:30px;left:470px;display:flex;color:var(--white);font-size:12.5px;font-weight:500}
  .nav a{color:inherit;text-decoration:none;position:absolute;white-space:nowrap}
  .call-tab{position:absolute;left:1008px;top:0;width:31px;height:70px;background:var(--green);border-radius:0 0 16px 16px;color:var(--white)}
  .call-tab span{position:absolute;left:8px;top:10px;font-size:8px;writing-mode:vertical-rl}
  .call-tab svg{position:absolute;left:3px;top:41px}
  .contact{position:absolute;left:1043px;top:20px;width:140px;color:var(--white);white-space:nowrap}
  .contact .phone{font-size:16px;font-weight:500;margin-left:13px}
  .contact .mail{font-size:9.5px;margin-top:3px;margin-left:6px}
  .frame{position:absolute;left:601px;top:128px;width:403px;height:358px;border:2px solid var(--white);border-left:none}
  .frame::before,.frame::after{content:"";position:absolute;left:0;width:2px;background:var(--white)}
  .frame::before{top:0;height:22px}
  .frame::after{bottom:0;height:22px}
  .headline{position:absolute;left:0;width:1200px;top:176px;text-align:center;color:var(--white);font-family:"Playfair Display",serif;font-weight:700;font-size:62px;line-height:68px}
  .lead{position:absolute;left:270px;width:660px;top:319px;text-align:center;color:var(--white);font-size:12px;line-height:19px;font-weight:300}
  .btn{position:absolute;top:386px;width:193px;height:44px;display:flex;align-items:center;justify-content:center;color:var(--white);font-size:14px;font-weight:500}
  .btn-call{left:399px;border:2px solid var(--white)}
  .btn-quote{left:606px;background:var(--green)}
  .arrow{position:absolute;top:307px}
  .scroll{position:absolute;left:580px;top:546px;width:40px;text-align:center;color:var(--white);font-size:9px}
  .scroll i{display:block;width:1px;height:18px;background:var(--white);margin:0 auto}
  .scroll b{display:block;width:14px;height:21px;border:1.5px solid var(--white);border-radius:7px;margin:3px auto}

  /* about */
  .side-label{position:absolute;left:16px;color:var(--navy-text);font-weight:300;font-size:34px;writing-mode:vertical-rl;transform:rotate(180deg);letter-spacing:1px}
  .about-label{top:722px}
  .about-num{position:absolute;left:22px;top:851px;color:var(--navy-text);font-weight:300;font-size:17px}
  .about-rule{position:absolute;left:0;top:875px;width:42px;height:1px;background:#9a9aa8}
  .quote{position:absolute;left:106px;top:720px;width:415px;color:var(--navy-text);font-style:italic;font-size:16px;line-height:22px}
  .about-body{position:absolute;left:106px;top:824px;width:432px;color:var(--body);font-size:11.5px;font-weight:300;line-height:17px}
  .about-body p+p{margin-top:18px}
  .btn-more{position:absolute;left:106px;top:953px;width:93px;height:31px;background:var(--navy);color:var(--white);font-size:10px;font-weight:500;display:flex;align-items:center;justify-content:center}
  .about-photo{position:absolute;left:666px;top:704px;width:393px;height:300px;border-radius:30px 30px 0 30px;
    background:linear-gradient(135deg,#b9bcc0 0%,#8e8c88 45%,#c7b7a3 100%)}

  /* studies */
  .studies{position:absolute;left:0;top:1086px;width:1200px;height:114px;background:var(--navy)}
  .studies-label{position:absolute;left:22px;top:79px;color:var(--white);font-weight:300;font-size:34px;writing-mode:vertical-rl;transform:rotate(180deg)}
  .studies-bar{position:absolute;left:99px;top:76px;width:211px;height:40px;background:var(--green)}
  .studies-photo{position:absolute;left:106px;top:83px;width:450px;height:40px;background:linear-gradient(180deg,#6f9fd0,#a8c6e6)}
  .studies-title{position:absolute;left:627px;top:94px;color:var(--white);font-family:"Playfair Display",serif;font-weight:700;font-size:27px;white-space:nowrap}
</style>
</head>
<body>
<div class="page">
  <section class="hero" role="img" aria-label="Aerial photograph of a residential neighbourhood with pools and trees">
    <div class="header-line"></div>
    <div class="brand"><span class="brand-dot"></span><span class="brand-name">Copper Ridge Reserves</span></div>
    <nav class="nav">
      <a style="left:0">HOME</a>
      <a style="left:80px">ABOUT OUR COMPANY</a>
      <a style="left:269px">RESERVE STUDIES</a>
      <a style="left:431px">CONTACT US</a>
    </nav>
    <div class="call-tab"><span>CALL</span>
      <svg width="25" height="25" viewBox="0 0 25 25"><circle cx="12.5" cy="12.5" r="11" fill="none" stroke="#fff" stroke-width="1.5"/><path d="M9 7.5l2 2.5-1.2 1.5c.8 1.6 1.9 2.7 3.5 3.5l1.5-1.2 2.5 2-1.3 1.8c-3.8-.5-7.2-3.9-7.8-7.8z" fill="#fff"/></svg>
    </div>
    <div class="contact"><div class="phone">(208) 555-0142</div><div class="mail">Dana@CopperRidge.example</div></div>
    <div class="frame"></div>
    <h1 class="headline">Your Financial Road Map<br>For The Next 30 Years!</h1>
    <p class="lead">The North Star is a constant in the night sky that seagoers have relied on for centuries.&nbsp; Navigating these stars is simply knowing the right points of origin and following the map that the heavens have laid before us.</p>
    <div class="btn btn-call">CALL (208) 555-0142</div>
    <div class="btn btn-quote">REQUEST QUOTE</div>
    <svg class="arrow" style="left:19px" width="30" height="34" viewBox="0 0 30 34"><path d="M8 1h21v32H8M8 1v9M8 33v-9M21 17H2M7 12l-5 5 5 5" fill="none" stroke="#fff" stroke-width="1.5"/></svg>
    <svg class="arrow" style="left:1153px" width="30" height="34" viewBox="0 0 30 34"><path d="M8 1h20v32H8M8 1v9M8 33v-9M2 17h19M16 12l5 5-5 5" fill="none" stroke="#fff" stroke-width="1.5"/></svg>
    <div class="scroll"><i></i><b></b>SCROLL<i style="margin-top:4px;height:26px"></i></div>
  </section>

  <div class="side-label about-label">ABOUT</div>
  <div class="about-num">01</div>
  <div class="about-rule"></div>
  <p class="quote">The North Star is a constant in the night sky that seagoers have relied on for centuries.&nbsp; Navigating these stars is simply knowing the right points of origin and following the map that the heavens have laid before us.</p>
  <div class="about-body">
    <p>We love the night sky!&nbsp; Amidst so much darkness and a seemingly chaotic expanse<br>of billions of stars, there is great order.</p>
    <p>Of all the constellations and distractions of<br>the beautiful sky, the North Star remains ever true, ever vigilant and ever rooted.<br>A financial plan should be equally so!</p>
  </div>
  <div class="btn-more">READ MORE</div>
  <div class="about-photo" role="img" aria-label="Photograph of a smiling analyst working at a laptop in a bright office"></div>

  <section class="studies">
    <div class="studies-label">ES</div>
    <div class="studies-bar"></div>
    <div class="studies-photo" role="img" aria-label="Photograph of a condominium building under a blue sky"></div>
    <h2 class="studies-title">HOA &amp; Condominium Studies</h2>
  </section>
</div>
</body>
</html>
```